STOREFRONT SIGNAGE/ NEW LOGO

Looking for someone to enhance my current sign idea. I own a pawn shop , which is also a gun shop. I want a catchy front sign, which will be a lighted box sign. I may want to incorporate some symbols or character symbology that highlight firearms, such as : guns, ammo, targets, scope retical , gold, diamonds, cash, watches and/or pawn balls, and im open to other ideas, but i do not want it too busy, i want it simple, with a twist. Attached, you will find a very basic design, showing the business name and the verbiage that I would like to be incorporated into the design. God bless and thank you. may the best design win !

```html
<!DOCTYPE html>
<html lang="en">
<head>
<meta charset="utf-8">
<title>Meridian Gold &amp; Gun Exchange – Storefront Sign</title>
<link rel="stylesheet" href="https://fonts.googleapis.com/css2?family=Montserrat:ital,wght@0,500;0,700;0,800;1,800&display=swap">
<style>
  :root {
    --gold: #c0922e;
    --black: #000000;
    --white: #ffffff;
    --grey: #dcdcdc;
    --grey-light: #eceef0;
    --backdrop: #e6e6e6;
    --font: "Montserrat", Arial, sans-serif;
  }
  * { margin: 0; padding: 0; box-sizing: border-box; }
  html, body {
    width: 1200px; height: 1148px; overflow: hidden;
    background: var(--backdrop);
    font-family: var(--font);
  }
  .sign {
    position: absolute; left: 40px; top: 462px;
    width: 1120px; height: 224px;
    overflow: hidden;
  }
  .sign-bg { position: absolute; inset: 0; width: 100%; height: 100%; }
  .sign > *:not(.sign-bg) { position: absolute; line-height: 1; white-space: nowrap; }

  /* left panel */
  .headline { font-weight: 800; color: var(--white); font-size: 43px; left: 21px; }
  .headline--gold { top: 18px; }
  .headline--gun { top: 128px; }
  .subline { font-weight: 800; font-style: italic; color: var(--gold); font-size: 31px; left: 21px; }
  .subline--first { top: 66px; }
  .subline--second { top: 173px; }
  .ampersand { font-weight: 700; color: var(--white); font-size: 22px; left: 21px; top: 102px; }
  .divider-rule { left: 49px; top: 112px; width: 192px; height: 1.5px; background: var(--white); }
  .icon-box {
    width: 31px; height: 31px; border: 1.5px solid var(--gold); border-radius: 4px;
  }
  .icon-box--gold { left: 174px; top: 26px; }
  .icon-box--gun { left: 142px; top: 134px; }

  /* centre */
  .brand-name {
    left: 535px; top: 49px; transform: translate(-50%, -50%);
    font-weight: 800; font-size: 32px; color: var(--black); letter-spacing: 1px;
  }
  .tag-rule { height: 1px; background: var(--gold); }
  .tag-rule--top { left: 329px; top: 96px; width: 430px; }
  .tag-rule--bottom { left: 313px; top: 130px; width: 430px; }
  .tagline {
    left: 535px; top: 112px; transform: translate(-50%, -50%);
    font-weight: 800; font-size: 18px; color: var(--black); letter-spacing: 0.6px;
  }
  .tagline em { font-style: italic; color: var(--gold); }
  .phone-number {
    left: 561px; top: 162px; transform: translate(-50%, -50%);
    font-weight: 800; font-style: italic; font-size: 27px; color: var(--white); letter-spacing: 1px;
  }
  .web-address {
    left: 535px; top: 197px; transform: translate(-50%, -50%);
    font-weight: 500; font-size: 12px; color: var(--black); letter-spacing: 3px;
  }

  /* right panel */
  .service-list { list-style: none; left: 942px; top: 23px; }
  .service {
    display: flex; align-items: center; height: 24px; margin-bottom: 15px;
    font-weight: 800; font-size: 21px; color: var(--white); letter-spacing: 1px;
  }
  .service svg { width: 24px; height: 24px; margin-right: 14px; flex: none; }
</style>
</head>
<body>
  <div class="sign">
    <svg class="sign-bg" viewBox="0 0 1772 354" preserveAspectRatio="none" aria-hidden="true">
      <rect width="1772" height="354" fill="var(--black)"/>
      <!-- left chevrons -->
      <polygon points="0,0 570,0 490,354 0,354" fill="var(--grey)"/>
      <polygon points="0,0 500,0 420,354 0,354" fill="var(--gold)"/>
      <polygon points="0,0 350,0 432,185 330,354 0,354" fill="var(--black)"/>
      <!-- centre -->
      <polygon points="565,0 1210,0 1280,180 1222,354 490,354 478,190" fill="var(--white)"/>
      <polygon points="400,354 478,190 565,354" fill="var(--grey-light)"/>
      <polygon points="1180,0 1270,0 1235,80" fill="var(--grey-light)"/>
      <!-- right chevrons -->
      <polygon points="1270,0 1300,0 1345,130 1320,354 1222,354 1280,180" fill="var(--grey)"/>
      <polygon points="1300,0 1390,0 1350,110 1470,354 1320,354 1345,130" fill="var(--gold)"/>
      <polygon points="1390,0 1772,0 1772,354 1470,354 1350,110" fill="var(--black)"/>
      <!-- phone plate -->
      <polygon points="628,228 710,228 690,287 610,287" fill="var(--black)"/>
      <polygon points="712,228 1086,228 1066,287 692,287" fill="var(--gold)"/>
      <path d="M647 246c2-3 5-3 6-1l5 7c1 2 0 4-2 5l-2 1c1 4 6 10 10 12l2-2c1-2 3-2 5 0l6 5c2 1 1 4-1 6-3 3-7 3-11 1-9-5-16-13-20-22-1-4 0-9 2-12z" fill="none" stroke="var(--white)" stroke-width="2"/>
    </svg>

    <span class="headline headline--gold">GOLD</span>
    <span class="icon-box icon-box--gold" role="img" aria-label="Gold bars icon"></span>
    <span class="subline subline--first">EXCHANGE</span>
    <span class="ampersand">&amp;</span>
    <span class="divider-rule"></span>
    <span class="headline headline--gun">GUN</span>
    <span class="icon-box icon-box--gun" role="img" aria-label="Handgun icon"></span>
    <span class="subline subline--second">EXCHANGE</span>

    <span class="brand-name">MERIDIAN</span>
    <span class="tag-rule tag-rule--top"></span>
    <span class="tagline">CASH FOR <em>GOLD</em>.....CASH FOR <em>GUNS</em></span>
    <span class="tag-rule tag-rule--bottom"></span>
    <span class="phone-number">555-013-027</span>
    <span class="web-address">WWW.MERIDIANPAWN.COM</span>

    <ul class="service-list">
      <li class="service"><svg viewBox="0 0 24 24"><rect x="1" y="1" width="22" height="22" rx="4" fill="none" stroke="var(--gold)" stroke-width="1.6"/><path d="M7 12.5l3.5 3.5L17 8" fill="none" stroke="var(--white)" stroke-width="2"/></svg>PAWN</li>
      <li class="service"><svg viewBox="0 0 24 24"><rect x="1" y="1" width="22" height="22" rx="4" fill="none" stroke="var(--gold)" stroke-width="1.6"/><path d="M7 12.5l3.5 3.5L17 8" fill="none" stroke="var(--white)" stroke-width="2"/></svg>BUY</li>
      <li class="service"><svg viewBox="0 0 24 24"><rect x="1" y="1" width="22" height="22" rx="4" fill="none" stroke="var(--gold)" stroke-width="1.6"/><path d="M7 12.5l3.5 3.5L17 8" fill="none" stroke="var(--white)" stroke-width="2"/></svg>SELL</li>
      <li class="service"><svg viewBox="0 0 24 24"><rect x="1" y="1" width="22" height="22" rx="4" fill="none" stroke="var(--gold)" stroke-width="1.6"/><path d="M7 12.5l3.5 3.5L17 8" fill="none" stroke="var(--white)" stroke-width="2"/></svg>TRADE</li>
      <li class="service"><svg viewBox="0 0 24 24"><rect x="1" y="1" width="22" height="22" rx="4" fill="none" stroke="var(--gold)" stroke-width="1.6"/><path d="M7 12.5l3.5 3.5L17 8" fill="none" stroke="var(--white)" stroke-width="2"/></svg>LAYAWAY</li>
    </ul>
  </div>
</body>
</html>
```